Book cover for book titled The Quiet Harbor's Drift Ledger

Need a book cover for a book size 5.25 x 8.
Title: The Quiet Harbor's Drift Ledger
Subtitle: 40 Habits You Might Shed on the Road to a Calmer Year in the Season of Change
Author: Dr. Marvin T. Okafor
Foreword by Leopold Vantrease, Ph.D.
The book cover should be white. I have uploaded 2 photos. The closeup with the hat should go on the front with the text. The one in the chair should go on the back. It will be the only thing on the back.

```html
<!DOCTYPE html>
<html lang="en">
<head>
<meta charset="utf-8">
<title>The Quiet Harbor's Drift Ledger — Cover Wrap</title>
<link href="https://fonts.googleapis.com/css2?family=Amatic+SC:wght@700&family=Oswald:wght@500;600&family=Raleway:wght@300&display=swap" rel="stylesheet">
<style>
  :root {
    --backdrop: #000000;
    --paper: #f7f7f7;
    --ink: #111111;
    --ink-soft: #3a3a3a;
    --accent-red: #a51d1d;
    --photo-dark: #0d0d0d;
    --photo-mid: #3b3d42;
    --white: #ffffff;
  }
  * { box-sizing: border-box; margin: 0; padding: 0; }
  html, body {
    width: 1200px; height: 1200px; overflow: hidden;
    background: var(--backdrop);
  }
  .wrap {
    position: absolute; left: 46px; top: 197px;
    width: 1108px; height: 805px;
    background: var(--paper);
    overflow: hidden;
  }
  /* Back cover */
  .back-photo {
    position: absolute; left: 83px; top: 98px;
    width: 416px; height: 563px;
    background: radial-gradient(ellipse at 50% 45%, #2a2a2e 0%, #5b5f6b 38%, #d9d9d9 70%, rgba(247,247,247,0) 100%);
  }
  /* Spine */
  .spine {
    position: absolute; left: 516px; top: 0;
    width: 66px; height: 805px;
  }
  .spine-title, .spine-author {
    position: absolute; left: 50%;
    writing-mode: vertical-rl;
    transform: translateX(-50%);
    color: var(--ink); white-space: nowrap;
  }
  .spine-title {
    top: 84px;
    font-family: "Amatic SC", cursive;
    font-size: 42px; letter-spacing: 1px;
  }
  .spine-author {
    top: 574px;
    font-family: "Oswald", sans-serif;
    font-weight: 500; font-size: 18px; letter-spacing: 0.5px;
  }
  /* Front cover */
  .front {
    position: absolute; left: 582px; top: 0;
    width: 526px; height: 805px;
  }
  .title {
    text-align: center; color: var(--ink);
    font-family: "Amatic SC", cursive; font-weight: 700;
    line-height: 1;
  }
  .title-top {
    position: absolute; top: 24px; left: 0; width: 100%;
    font-size: 56px;
  }
  .title-main {
    position: absolute; top: 80px; left: 0; width: 100%;
    font-size: 122px; letter-spacing: 1px;
  }
  .subtitle {
    position: absolute; top: 222px; left: 0; width: 100%;
    text-align: center;
    font-family: "Raleway", sans-serif; font-weight: 300;
    font-size: 22px; line-height: 31px;
    text-transform: uppercase; color: var(--ink-soft);
  }
  .subtitle .accent { color: var(--accent-red); }
  .front-photo {
    position: absolute; left: 0; top: 320px;
    width: 526px; height: 485px;
    background: linear-gradient(180deg, rgba(247,247,247,0) 0%, #c9c3b0 18%, var(--photo-mid) 48%, var(--photo-dark) 80%);
  }
  .credits {
    position: absolute; left: 0; width: 100%;
    text-align: center; color: var(--white);
    font-family: "Oswald", sans-serif; text-transform: uppercase;
  }
  .author { top: 716px; font-size: 36px; font-weight: 600; }
  .foreword { top: 760px; font-size: 21px; font-weight: 500; }
</style>
</head>
<body>
  <div class="wrap">
    <section class="back">
      <div class="back-photo" role="img" aria-label="Photo of the author in sunglasses and a face mask seated in a white armchair, straw boater hat by his red sneakers, faint grey virus emblem behind his head"></div>
    </section>

    <section class="spine">
      <div class="spine-title">THE QUIET HARBOR'S DRIFT LEDGER</div>
      <div class="spine-author">DR. MARVIN T. OKAFOR</div>
    </section>

    <section class="front">
      <h1 class="title">
        <span class="title-top">THE QUIET HARBOR'S</span>
        <span class="title-main">DRIFT LEDGER</span>
      </h1>
      <p class="subtitle">
        40 Habits You Might Shed on the Road<br>
        to a Calmer Year<br>
        <span class="accent">in the Season of Change</span>
      </p>
      <div class="front-photo" role="img" aria-label="Close-up photo of the author in a straw boater hat with red and navy band, tinted glasses and a grey face mask, on a dark background"></div>
      <p class="credits author">Dr. Marvin T. Okafor</p>
      <p class="credits foreword">Foreword by Leopold Vantrease, Ph.D.</p>
    </section>
  </div>
</body>
</html>
```